Looking for new corporate web site design ideas

Hi everyone,

We're looking for a new web 2.0 style design for our main corporate website Quorvan.com. This design contest will be for a main home page design for the new Quorvan.com web site, as well as a single sub page (product page).

**IMPORTANT** The old site design focused heavily on our initial business model (generating leads for mortgage and insurance clients). While we still generate leads as a portion of the business, we want the new web site to be much more reflective of our whole business.

The company is now split into four verticals. They are:

Lead Generation (Our initial businesses model. We will highlight: VitaPathSource.com, & HomeLoanPathSource.com ).

Lead Analytics (3 products - BrindQ, TruMARK, oPulse).

Data Services / Licensing (Selling bulk data on 143 Million homeowners in the USA).

Swift Bridge (Telephone hot transfer leads: Swiftbridge.co).

Intelligent Web Sites (StreetSmartly.com as well as three others).

My plan is to have all of our products lines (14 in total) fit within the above.

***VERY IMPORTANT** We will need a way to be able to show the above 5 categories as well as showcasing some of the products on the home page. We will then link off to sub pages within Quorvan.com and finally link out to the individual products own web sites.

We like icon's / pictures as a way to communicate complex products quickly. Also, we will be using much less text on this site (vs. the current version).

Our corporate color's are set in the current logo (see the www.quorvan.com) site. We are open to new colors for the site, but the logo is trademarked, so make sure to have your design allow for the current logo colors.

The final design should communicate that we are a company with a large number of products (14+) and websites (over 200). We want to be known for all of the products that we offer, not just as our name implies (Quorvan) lead generation!

Target Market(s)

Our target market is business to business. We currently sell/ license our products to mortgage and insurance companies all across the USA. We will be expanding into real estate in 2014.

We do not sell to consumers, so please be more corporate than consumer!

Industry/Entity Type

Insurance

Font styles to use
Sans Serif

Requirements
Must have
• All designs should have the ability to clearly display and communicate to the user the five product categories that we have:

Lead Generation
Lead Analytics
Data Services / Licensing
Swift Bridge
Intelligent Web Sites.

We have way too much text currently on our web site. Our new design should rely on icons and pictures to tell the story of our products, with text only as simple explanations.

We have a style guide for font use and color's that I have just added to the brief. Please maintain your design using our style guide for font's etc.

We have 14 product products lines (think Fizzo corp or KVT or Pearl). We want an effective way or showing that the company is much bigger than just leads!
Nice to have
• We're a company that has 17 years of history on the Internet (since 1996). We'd like to communicate that fact to give our users a sense that we're here to stay.

Should not have
• We're not looking for a simply facelift for the current Quorvan.com site! We're looking for a much more web 2.0 type of design!

```html
<!DOCTYPE html>
<html lang="en">
<head>
<meta charset="utf-8">
<title>Quorvan.com</title>
<link href="https://fonts.googleapis.com/css2?family=Lato:wght@300;400;700&display=swap" rel="stylesheet">
<style>
:root{
  --red:#c8281e;
  --green:#45a048;
  --ink:#1d1d1d;
  --grey:#8e8e8e;
  --panel:#f1f1f1;
  --soft:#f7f7f7;
  --black:#000;
  --bar:#1a1a1a;
  --muted:#4a4a4a;
}
*{margin:0;padding:0;box-sizing:border-box}
html,body{width:863px;height:1200px;overflow:hidden;background:#fff}
body{font-family:'Lato',sans-serif;color:var(--ink);position:relative}
.abs{position:absolute}
/* header */
.header{position:absolute;left:0;top:0;width:863px;height:61px;background:#fff;border-bottom:2px solid #e2e2e2}
.brand{left:214px;top:21px;font-size:17px;font-weight:700;letter-spacing:-.3px}
.phones{right:207px;top:9px;font-size:6.5px;color:var(--red);display:flex;gap:14px}
.phones span{display:flex;align-items:center;gap:3px}
.nav{right:207px;top:30px;font-size:7.6px;display:flex;gap:9px;color:var(--ink)}
.nav i{font-style:normal;color:#bbb}
/* hero */
.hero{left:0;top:62px;width:863px;height:246px;background:linear-gradient(#e4e4e4,#f1f1f1)}
.product-mark{left:277px;top:102px;width:85px;height:80px;background:var(--green);border-radius:6px}
.hero-copy{left:216px;top:193px;width:212px;font-size:7.8px;line-height:10.5px;font-weight:300;color:#111}
.btn{top:254px;height:24px;width:89px;color:#fff;font-size:9.5px;display:flex;align-items:center;justify-content:center;letter-spacing:.2px}
.btn-more{left:228px;background:var(--green)}
.btn-dl{left:322px;background:var(--red)}
.hero-ring{left:432px;top:73px;width:224px;height:224px;border-radius:50%;background:var(--red);padding:14px}
.hero-photo{width:196px;height:196px;border-radius:50%;overflow:hidden;position:relative;background:radial-gradient(circle at 50% 38%,#f2dcc6 0,#e7c9a8 28%,#f3f0ec 60%,#e9e9e9 100%)}
.hero-tag{position:absolute;left:0;bottom:0;width:100%;height:46px;background:#111;color:#fff;font-size:10.5px;font-weight:700;display:flex;align-items:flex-start;justify-content:center;padding-top:10px;gap:4px}
.hero-tag b{width:9px;height:9px;background:var(--green);margin-top:2px}
.arrow{top:173px;width:23px;height:23px;border-radius:50%;background:#9a9a9a}
/* products */
.section-title{width:863px;text-align:center;font-size:24px;font-weight:400;letter-spacing:.3px}
.section-text{left:210px;width:443px;text-align:center;font-size:7.5px;line-height:10px;color:#333;font-weight:300}
.cat{top:438px;width:86px;text-align:center}
.cat-circle{width:86px;height:86px;border-radius:50%;background:var(--grey);display:flex;align-items:center;justify-content:center}
.cat.active .cat-circle{background:#fff;border:4px solid var(--red)}
.cat-label{margin-top:14px;font-size:6.6px;color:var(--ink)}
.cat.active .cat-label{color:var(--red)}
.panel{left:206px;top:558px;width:451px;height:152px;background:var(--panel)}
.panel-notch{left:242px;top:550px;width:0;height:0;border-left:8px solid transparent;border-right:8px solid transparent;border-bottom:8px solid var(--panel)}
.panel-col{top:20px;width:188px}
.panel-head{display:flex;align-items:center;gap:4px;font-size:8.6px;margin-bottom:10px}
.panel-head b{width:14px;height:14px;border-radius:50%;background:#222}
.panel-col p{font-size:5.4px;line-height:7.6px;color:#444;margin-bottom:7px}
.panel-rule{left:224px;top:26px;width:0;height:102px;border-left:1px dashed #c8c8c8}
/* clients */
.clients{left:0;top:740px;width:863px;height:235px;background:var(--soft)}
.client{font-size:11px;font-weight:700;color:#a9a9a9;width:110px;text-align:center}
/* footer */
.footer{left:0;top:975px;width:863px;height:199px;background:var(--black);color:#ddd}
.f-head{top:20px;font-size:7px;letter-spacing:.2px}
.f-list{top:42px;font-size:5.2px;line-height:10.4px;color:var(--muted)}
.f-about{top:42px;width:142px;font-size:5.2px;line-height:8.7px;color:var(--muted)}
.social{left:573px;top:100px;display:flex;gap:4px}
.social b{width:11px;height:11px;background:#666;border-radius:2px}
.tweet{left:211px;top:139px;width:439px;height:31px;background:#2a2a2a;border-radius:3px;font-size:5.3px;color:#fff;padding:12px 14px}
.tweet a{color:var(--red);text-decoration:none}
.tweet-tail{left:222px;top:170px;width:0;height:0;border-top:6px solid #2a2a2a;border-right:7px solid transparent}
.bottom{left:0;top:1174px;width:863px;height:26px;background:var(--bar);font-size:5.2px;color:#666}
</style>
</head>
<body>

<header class="header">
  <div class="abs brand">Quorvan.com</div>
  <div class="abs phones">
    <span><svg width="7" height="7" viewBox="0 0 10 10"><path d="M2 0l2 2-1 2c1 1 2 2 3 3l2-1 2 2-2 2C4 10 0 6 0 2z" fill="#c8281e"/></svg>(866) 410-5582</span>
    <span><svg width="7" height="7" viewBox="0 0 10 10"><circle cx="5" cy="3" r="2.5" fill="#c8281e"/><path d="M0 10c0-3 2-4.5 5-4.5s5 1.5 5 4.5z" fill="#c8281e"/></svg>(866) 410-5582</span>
  </div>
  <nav class="abs nav"><span>COMPANY</span><i>|</i><span>LEADS</span><i>|</i><span>DATA</span><i>|</i><span>RESOURCES</span><i>|</i><span>CONTACT</span></nav>
</header>

<section class="abs hero"></section>
<div class="abs arrow" style="left:43px"><svg width="23" height="23" viewBox="0 0 23 23"><path d="M13 6l-6 5.5 6 5.5z" fill="#fff"/></svg></div>
<div class="abs arrow" style="left:796px"><svg width="23" height="23" viewBox="0 0 23 23"><path d="M10 6l6 5.5-6 5.5z" fill="#fff"/></svg></div>
<div class="abs product-mark"></div>
<p class="abs hero-copy">Swift Bridge is a next generation platform developed to drive real time connections with companies and their audience. We are currently in beta testing, the full version will be available soon.</p>
<a class="abs btn btn-more">READ MORE</a>
<a class="abs btn btn-dl">DOWNLOAD</a>
<div class="abs hero-ring">
  <div class="hero-photo" role="img" aria-label="Photo of a smiling call centre agent wearing a headset">
    <div class="hero-tag"><b></b>Swift Bridge</div>
  </div>
</div>

<h2 class="abs section-title" style="top:344px">OUR PRODUCTS</h2>
<p class="abs section-text" style="top:386px">To steer through these turbulent times, it's more important than ever to know more about every lead, every opportunity, and every customer. To thrive, you need to work smarter, get efficient, and stay lean. You need to have options, limit the chances that you take, and pick your lead and marketing partners carefully.</p>

<div class="abs cat active" style="left:207px">
  <div class="cat-circle"><svg width="38" height="38" viewBox="0 0 38 38" fill="none" stroke="#c8281e" stroke-width="3.5"><path d="M8 19a11 11 0 0 1 19-7.5"/><path d="M30 19a11 11 0 0 1-19 7.5"/><path d="M24 10h5V5M14 28H9v5"/><circle cx="19" cy="16" r="3" fill="#c8281e" stroke="none"/><path d="M13 25c0-4 3-5 6-5s6 1 6 5z" fill="#c8281e" stroke="none"/></svg></div>
  <div class="cat-label">Lead Generation</div>
</div>
<div class="abs cat" style="left:298px">
  <div class="cat-circle"><svg width="40" height="40" viewBox="0 0 40 40" fill="none" stroke="#fff" stroke-width="2.5"><rect x="6" y="7" width="28" height="20"/><path d="M10 22l6-7 5 4 8-9"/><path d="M20 27v5M13 36l7-4 7 4"/></svg></div>
  <div class="cat-label">Lead Analytics</div>
</div>
<div class="abs cat" style="left:388px">
  <div class="cat-circle"><svg width="36" height="36" viewBox="0 0 36 36" fill="none" stroke="#fff" stroke-width="2.5"><rect x="8" y="20" width="16" height="10"/><path d="M10 20l10-12M13 20l13-10M16 20l13-7M24 3l2 2M28 7l2 2"/></svg></div>
  <div class="cat-label">Data Services / Licensing</div>
</div>
<div class="abs cat" style="left:479px">
  <div class="cat-circle"><svg width="36" height="36" viewBox="0 0 36 36"><path d="M18 4c8 0 14 5.5 14 13s-6 13-14 13c-2 0-4-.4-5.5-1L6 32l2-6c-2-2.5-4-5.5-4-9C4 9.5 10 4 18 4z" fill="#fff"/><circle cx="18" cy="14" r="3.5" fill="#8e8e8e"/><path d="M11 24c0-4 3-6 7-6s7 2 7 6z" fill="#8e8e8e"/></svg></div>
  <div class="cat-label">Swift Bridge</div>
</div>
<div class="abs cat" style="left:571px">
  <div class="cat-circle"><svg width="38" height="38" viewBox="0 0 38 38" fill="none" stroke="#fff" stroke-width="3"><rect x="5" y="6" width="28" height="19" rx="1"/><path d="M19 25v5M11 32h16"/></svg></div>
  <div class="cat-label">Intelligent Web Sites</div>
</div>

<div class="abs panel-notch"></div>
<div class="abs panel">
  <div class="abs panel-col" style="left:17px">
    <div class="panel-head"><b></b>VitaPathSource</div>
    <p>Qualified life insurance prospects delivered in real time, screened for intent and matched to your agents by region and product.</p>
    <p>Every record is verified before delivery, with filters for age, coverage amount and state, so your team spends time on buyers who are ready to talk today.</p>
  </div>
  <div class="abs panel-rule"></div>
  <div class="abs panel-col" style="left:249px">
    <div class="panel-head"><b></b>HomeLoanPathSource</div>
    <p>Exclusive mortgage prospects captured across our network, scored on loan type, credit band and property value before they reach your desk.</p>
    <p>Set daily caps, choose purchase or refinance, and route each record straight into your CRM so loan officers can respond within minutes of the request.</p>
  </div>
</div>

<section class="abs clients">
  <h2 class="abs section-title" style="top:52px">MEET SOME OF OUR CLIENTS</h2>
  <p class="abs section-text" style="top:93px">Whether you are looking for mortgage leads or insurance Quorvan.com &reg; is your source.<br>Go with a name you can trust, Quorvan.com!</p>
  <div class="abs client" style="left:218px;top:142px">Veltrana</div>
  <div class="abs client" style="left:325px;top:142px">Corvine</div>
  <div class="abs client" style="left:435px;top:142px">Halbrook</div>
  <div class="abs client" style="left:546px;top:142px">Wexmoor</div>
  <div class="abs client" style="left:218px;top:182px">Brisko Loans</div>
  <div class="abs client" style="left:325px;top:182px">NUV</div>
  <div class="abs client" style="left:435px;top:182px">lendpath</div>
  <div class="abs client" style="left:546px;top:182px">Ostrel Life</div>
</section>

<footer class="abs footer">
  <div class="abs f-head" style="left:209px">ABOUT THE COMPANY</div>
  <p class="abs f-about" style="left:209px">Quorvan has connected buyers and sellers online since 1996, building data, analytics and lead products for mortgage and insurance firms across the country. Our network of sites reaches millions of homeowners every month.</p>
  <div class="abs f-head" style="left:385px">PRODUCTS</div>
  <div class="abs f-list" style="left:385px">TruMARK<br>BrindQ<br>RenewQ<br>Swift Bridge</div>
  <div class="abs f-head" style="left:462px">OUR SERVICES</div>
  <div class="abs f-list" style="left:462px">Life Insurance Leads<br>Long Term Care Leads<br>Homeowner Insurance Leads<br>Auto Insurance Leads<br>Health Insurance Leads<br>Disability Insurance Leads<br>Annuity Leads</div>
  <div class="abs f-head" style="left:572px">CONTACT</div>
  <div class="abs f-list" style="left:572px">T: 866-410-5582<br>E: inquiries@quorvan.com<br><span style="display:block;height:4px"></span><span style="line-height:7px;display:block">214 Harbor Crest Way Suite 300<br>Alder Bay CA 90417</span></div>
  <div class="abs social"><b></b><b></b><b></b><b></b></div>
  <div class="abs tweet">@Quorvan 3 Rules You Must Follow If You Want Your Company to Be Exceptional <a>http://qv.to/8kTmA2</a></div>
  <div class="abs tweet-tail"></div>
</footer>

<div class="abs bottom">
  <span class="abs" style="left:207px;top:10px">Copyright &copy; 2014. All Rights Reserved.</span>
  <span class="abs" style="right:207px;top:10px">Privacy Policy - Legal Disclaimers</span>
</div>

</body>
</html>
```